Catalog for Varno Gearworks featuring all the model of Pierre Calvet Roof Top Tents

Creative Catalog to hand out to visitors of Outdoor Expos. The Catalog branding will be VARNO Gearworks Featuring
Pierre Calvet Roof Top Tents / Exclusive Dealer
Having two pages each for each of the tent models showing multiple pictures and specifications:
Horizon
Summit
Canopy
Nomad / Nomad XXL
Ranger
Long Trail
and then multiple pages as necessary for accessories, Custom colors, and company information.

Target Market(s)

Adventure Travelers

Font styles to use
Sans Serif

Requirements
Must have
• 5.5" x 8.5" horizontal layout ideally around 20 pages (16 + covers)
Catalog must have the feel, logos and imagery of our VARNO gearworks branding: https://www.facebook.com/VarnoGear/

would want phone number: (513) 762-1938 and website www.Varno.Gear at the bottom of every other page. I would like to have 2 pages for EACH tent model. one page showing an environmental shot of the tent. photos can be found here:
https://www.pierrecalvet.example/en/galleries/
https://www.facebook.com/PierreCalvetOfficial/photos/?ref=page_internal
the 2nd page showing actual product photos description and specifications:
https://www.pierrecalvet.example/en/products/

```html
<!DOCTYPE html>
<html lang="en">
<head>
<meta charset="utf-8">
<title>Varno Gearworks – Roof Top Tent Catalog</title>
<link rel="stylesheet" href="https://fonts.googleapis.com/css2?family=Montserrat:wght@400;500;600;700;800&family=Open+Sans:wght@400;600&display=swap">
<style>
:root{
  --stage:#dedede;
  --navy:#0d1627;
  --navy-2:#16233b;
  --blue:#1f8fe6;
  --blue-light:#4fb3ff;
  --orange:#ec7a1c;
  --ink:#3a3f47;
  --muted:#8a9099;
  --paper:#ffffff;
  --thumb:#f3f4f6;
  --head:"Montserrat",sans-serif;
  --body:"Open Sans",sans-serif;
}
*{box-sizing:border-box;margin:0;padding:0}
html,body{width:1200px;height:4000px;overflow:hidden}
body{background:var(--stage);font-family:var(--body);color:var(--ink);
  display:flex;flex-direction:column;align-items:center;padding-top:170px;gap:0}

/* ---------- covers ---------- */
.cover{width:900px;height:582px;position:relative;overflow:hidden;background:var(--navy);
  box-shadow:0 18px 40px rgba(0,0,0,.18)}
.cover-front{margin-bottom:230px}
.cover-back{margin-bottom:330px}
.front-pattern{position:absolute;inset:0;
  background:linear-gradient(135deg,#13243f 0%,#0b1322 55%,#10203a 100%)}
.front-photo{position:absolute;inset:0;
  clip-path:polygon(0 0,100% 0,100% 79%,52% 79%,0 34%);
  background:linear-gradient(160deg,#d4d4d4 0%,#a9a9a9 45%,#6e6e6e 80%,#4a4a4a 100%)}
.brand{display:flex;align-items:center;gap:9px;font-family:var(--head);font-weight:700;
  letter-spacing:.04em;white-space:nowrap}
.brand-mark{width:14px;height:14px;background:var(--blue)}
.front-photo-brand{position:absolute;left:230px;top:96px;font-size:30px;color:var(--navy)}
.front-photo-brand .brand-mark{width:24px;height:24px}
.dealer{position:absolute;right:60px;top:42px;font-family:var(--head);font-weight:500;
  color:#fff;font-size:15px;line-height:1.35;text-align:right;letter-spacing:.04em}
.tagline{position:absolute;right:54px;bottom:56px;text-align:right;font-family:var(--head);color:#fff}
.tagline-main{font-size:34px;font-weight:800;letter-spacing:.03em}
.tagline-main span{color:var(--blue-light)}
.tagline-url{font-size:14px;font-weight:600;letter-spacing:.12em;margin-top:6px}

.back-shape{position:absolute;inset:0;
  clip-path:polygon(52% 0,100% 0,100% 100%,72% 100%,40% 42%);
  background:linear-gradient(160deg,#7cc8ff 0%,#2f9cf0 45%,#1566b4 100%)}
.back-line{position:absolute;left:0;top:0;width:100%;height:100%}
.back-brand{position:absolute;left:70px;top:200px;font-size:32px;color:#fff}
.back-brand .brand-mark{width:22px;height:22px}
.back-contact{position:absolute;left:70px;bottom:60px;font-family:var(--head);color:#fff;font-size:14px;line-height:1.9}
.contact-row{display:flex;align-items:center;gap:10px}
.social{display:flex;gap:8px;align-items:center}
.social i{width:18px;height:18px;border-radius:50%;background:var(--blue);display:block}

/* ---------- spreads ---------- */
.spread{display:flex;width:1100px;height:356px;margin-bottom:110px;
  box-shadow:0 16px 34px rgba(0,0,0,.16)}
.page{width:550px;height:356px;position:relative;overflow:hidden;background:var(--paper)}
.page-left{box-shadow:inset -14px 0 18px -14px rgba(0,0,0,.25)}
.page-right{box-shadow:inset 14px 0 18px -14px rgba(0,0,0,.25)}

.photo{position:absolute}
.cfg-title{position:absolute;font-family:var(--head);font-weight:700;font-size:20px;color:#fff;white-space:nowrap}
.cfg-title span{color:var(--orange)}
.sizes{position:absolute;width:96px;background:var(--navy);font-family:var(--head);font-size:5.5px;color:#fff;padding:4px 5px}
.sizes-head{background:#fff;color:var(--navy);font-weight:700;text-align:center;padding:2px 0;margin-bottom:3px;letter-spacing:.05em}
.sizes-row{display:flex;gap:6px;line-height:1.6}
.sizes-row b{color:var(--orange);font-weight:600;width:16px}
.thumbs{position:absolute;display:grid;gap:8px}
.thumb{background:var(--paper);border:1px solid #e4e6ea;display:flex;align-items:center;justify-content:center}
.thumb i{display:block;width:72%;height:66%;background:linear-gradient(150deg,#9aa0a8,#3c424a);
  clip-path:polygon(8% 100%,48% 4%,96% 100%)}
.thumb.flat i{height:22%;clip-path:none;border-radius:3px;background:linear-gradient(180deg,#f2f2f2,#b9bcc2)}
.thumb.box i{clip-path:polygon(10% 100%,18% 8%,82% 8%,92% 100%)}
.copy{position:absolute;font-size:6.4px;line-height:1.55;color:var(--ink)}
.copy p+p{margin-top:6px}
.foot{position:absolute;left:22px;right:18px;bottom:14px;display:flex;align-items:center;gap:10px}
.foot .brand{font-size:13px;color:var(--navy)}
.foot.on-dark .brand{color:#fff}
.foot-line{flex:1;height:1px;background:var(--orange);opacity:.6}
.url-pill{background:var(--orange);color:#fff;font-family:var(--head);font-weight:600;font-size:6.5px;padding:3px 9px;border-radius:8px;letter-spacing:.05em}
.page-num{width:13px;height:13px;border-radius:50%;background:var(--navy);color:#fff;font-family:var(--head);font-size:5.5px;display:flex;align-items:center;justify-content:center}

/* intro page */
.intro-panel{position:absolute;left:0;top:0;width:230px;height:100%;background:var(--navy);padding:24px 18px;color:#dfe6f2}
.intro-title{font-family:var(--head);font-weight:500;font-size:16px;color:#fff;letter-spacing:.02em}
.intro-title span{color:var(--orange);font-weight:700}
.intro-text{font-size:6.2px;line-height:1.55;margin-top:8px}
.intro-lead{font-family:var(--head);font-weight:700;font-size:6.4px;color:#fff;margin:8px 0 5px}
.intro-list{list-style:none;font-size:5.9px;line-height:1.45}
.intro-list li{position:relative;padding-left:11px;margin-bottom:5px}
.intro-list li::before{content:"";position:absolute;left:0;top:1px;width:6px;height:6px;border-radius:50%;background:var(--orange)}
</style>
</head>
<body>

<!-- Front cover -->
<section class="cover cover-front" aria-label="Front cover">
  <div class="front-pattern" role="img" aria-label="Dark navy texture with glowing blue geometric line pattern"></div>
  <div class="front-photo" role="img" aria-label="Black and white photo of a pickup truck with an opened roof top tent and awning in a landscape"></div>
  <div class="brand front-photo-brand"><i class="brand-mark"></i>VARNO Gearworks</div>
  <div class="dealer">Pierre Calvet<br>Roof Top Tents<br>Exclusive Dealer</div>
  <div class="tagline">
    <div class="tagline-main">OWN THE <span>OUTDOORS</span></div>
    <div class="tagline-url">WWW.VARNO.EXAMPLE</div>
  </div>
</section>

<!-- Back cover -->
<section class="cover cover-back" aria-label="Back cover">
  <div class="back-shape" role="img" aria-label="Large faceted blue crystal shape"></div>
  <svg class="back-line" viewBox="0 0 900 582" aria-hidden="true">
    <line x1="360" y1="244" x2="648" y2="582" stroke="#1f8fe6" stroke-width="4"/>
    <line x1="468" y1="0" x2="360" y2="244" stroke="#1f8fe6" stroke-width="4"/>
  </svg>
  <div class="brand back-brand"><i class="brand-mark"></i>VARNO Gearworks</div>
  <div class="back-contact">
    <div class="contact-row">
      <svg width="14" height="14" viewBox="0 0 24 24" aria-hidden="true"><path fill="#1f8fe6" d="M6.6 10.8a15 15 0 0 0 6.6 6.6l2.2-2.2c.3-.3.7-.4 1-.2 1.1.4 2.3.6 3.6.6.6 0 1 .4 1 1V20c0 .6-.4 1-1 1A17 17 0 0 1 3 4c0-.6.4-1 1-1h3.5c.6 0 1 .4 1 1 0 1.3.2 2.5.6 3.6.1.3 0 .7-.2 1z"/></svg>
      (513) 762-1938
    </div>
    <div class="contact-row">
      <svg width="14" height="14" viewBox="0 0 24 24" aria-hidden="true"><circle cx="12" cy="12" r="9" fill="none" stroke="#1f8fe6" stroke-width="2"/><path d="M3 12h18M12 3c3 3 3 15 0 18M12 3c-3 3-3 15 0 18" fill="none" stroke="#1f8fe6" stroke-width="1.6"/></svg>
      www.Varno.Gear
    </div>
    <div class="contact-row"><span class="social"><i></i><i></i><i></i></span> follow us</div>
  </div>
</section>

<!-- Spread 1 -->
<section class="spread">
  <article class="page page-left">
    <div class="photo" style="left:230px;top:0;right:0;bottom:0;background:linear-gradient(180deg,#3b2a6b 0%,#a04b9c 35%,#e07a8c 55%,#8a6a4a 75%,#c08a4a 100%)" role="img" aria-label="Sunset sky in purple and pink over a golden meadow"></div>
    <div class="intro-panel">
      <h2 class="intro-title">HARD <span>SHELL TENTS</span></h2>
      <p class="intro-text">Our hard shell roof tents are trusted around the world by generations of travelers and explorers. They are built not only for top quality but as a shelter that is comfortable and resistant to extreme climates, easy to use and made in Europe.</p>
      <p class="intro-lead">Among the many advantages we note:</p>
      <ul class="intro-list">
        <li>360° panoramic vision, to avoid the boxed feeling of other tents.</li>
        <li>Thick, dense mattresses that give you the comfort of home.</li>
        <li>Automatic opening assisted by gas struts, open in seconds.</li>
        <li>Breathable, blackout, double insulated fabric for all seasons.</li>
        <li>Solar ventilation that limits condensation inside the tent.</li>
        <li>Strong resistance to wind thanks to the locking arms.</li>
        <li>3-year warranty.</li>
      </ul>
    </div>
    <div class="foot on-dark"><div class="brand"><i class="brand-mark"></i>VARNO Gearworks</div><span class="foot-line" style="opacity:0"></span><span class="url-pill">WWW.VARNO.EXAMPLE</span><span class="page-num">02</span></div>
  </article>
  <article class="page page-right">
    <div class="photo" style="left:0;top:0;right:0;height:135px;background:linear-gradient(180deg,#0d1833 0%,#1d2f5a 55%,#5a6a86 85%,#c9ced8 100%)" role="img" aria-label="Starry night sky over snowy mountains"></div>
    <h2 class="cfg-title" style="left:22px;top:22px">Configurator <span>Horizon</span></h2>
    <div class="sizes" style="right:18px;top:16px"><div class="sizes-head">AVAILABLE SIZES</div><div class="sizes-row"><b>STD</b>130 x 210 CM</div><div class="sizes-row"><b>XXL</b>160 x 210 CM</div></div>
    <div class="thumbs" style="left:22px;right:22px;top:100px;grid-template-columns:repeat(4,1fr);height:86px">
      <div class="thumb" role="img" aria-label="Tent product photo, side view"><i></i></div>
      <div class="thumb" role="img" aria-label="Tent product photo, rear view"><i></i></div>
      <div class="thumb" role="img" aria-label="Tent product photo, open front"><i></i></div>
      <div class="thumb box" role="img" aria-label="Tent product photo, interior"><i></i></div>
    </div>
    <div class="copy" style="left:22px;right:22px;top:212px">
      <p>Built on the concept of the shell opening, the Pierre Calvet Horizon is the fastest of our models in terms of opening and closing. In its category it offers the best waterproofness and the best wind resistance on the market.</p>
      <p>The compact model in the line of roof top tents, it offers all the features of the larger models in a size that is easy to manage.</p>
    </div>
    <div class="foot"><div class="brand"><i class="brand-mark"></i>VARNO Gearworks</div><span class="foot-line"></span><span class="url-pill">WWW.VARNO.EXAMPLE</span><span class="page-num">03</span></div>
  </article>
</section>

<!-- Spread 2 -->
<section class="spread">
  <article class="page page-left">
    <div class="photo" style="left:0;top:0;right:0;height:135px;background:linear-gradient(180deg,#8a8fa0 0%,#c4b8a8 40%,#6f7a8c 70%,#2d3a52 100%)" role="img" aria-label="Snow capped mountain range under a cloudy dusk sky"></div>
    <h2 class="cfg-title" style="left:22px;top:22px">Configurator <span>Summit</span></h2>
    <div class="sizes" style="right:18px;top:16px"><div class="sizes-head">AVAILABLE SIZES</div><div class="sizes-row"><b>STD</b>130 x 210 CM</div><div class="sizes-row"><b>XXL</b>160 x 210 CM</div></div>
    <div class="thumbs" style="left:22px;right:22px;top:100px;grid-template-columns:repeat(4,1fr);height:86px">
      <div class="thumb" role="img" aria-label="Tent product photo, side view"><i></i></div>
      <div class="thumb" role="img" aria-label="Tent product photo, dark shell"><i></i></div>
      <div class="thumb box" role="img" aria-label="Tent product photo, interior"><i></i></div>
      <div class="thumb flat" role="img" aria-label="Tent product photo, closed shell"><i></i></div>
    </div>
    <div class="copy" style="left:22px;right:22px;top:212px">
      <p>Just as fast as the Horizon in terms of opening and closing, the Pierre Calvet Summit is marked by its luggage carrier which can hold a load of 25kg. Perfect for a spare tire or the walls of an awning.</p>
      <p>The tent opens in less than 1 minute through two hydraulic cylinders mounted on bearings. It can be closed by one person in less than 1 minute. A built in elastic band around the canvas keeps it inside the tent.</p>
    </div>
    <div class="foot"><div class="brand"><i class="brand-mark"></i>VARNO Gearworks</div><span class="foot-line"></span><span class="url-pill">WWW.VARNO.EXAMPLE</span><span class="page-num">04</span></div>
  </article>
  <article class="page page-right">
    <div class="photo" style="left:0;top:0;width:290px;bottom:0;background:linear-gradient(180deg,#1c2e5c 0%,#3a5a9a 35%,#5b6fb0 55%,#b04fb4 75%,#d35fc0 100%)" role="img" aria-label="Blue mountain ridges above a field of pink wildflowers"></div>
    <h2 class="cfg-title" style="left:22px;top:22px">Configurator <span>Canopy</span></h2>
    <div class="sizes" style="left:22px;top:52px"><div class="sizes-head">AVAILABLE SIZES</div><div class="sizes-row"><b>STD</b>140 x 220 CM</div></div>
    <div class="thumbs" style="left:306px;right:18px;top:18px;grid-template-columns:1fr 1fr;grid-template-rows:80px 80px">
      <div class="thumb box" role="img" aria-label="Tent product photo, front open"><i></i></div>
      <div class="thumb box" role="img" aria-label="Tent product photo, dark canvas"><i></i></div>
      <div class="thumb" role="img" aria-label="Tent product photo, side view"><i></i></div>
      <div class="thumb flat" role="img" aria-label="Tent product photo, closed shell"><i></i></div>
    </div>
    <div class="copy" style="left:306px;right:18px;top:200px">
      <p>Taking again the concept of the opening in shell of the Horizon, the Pierre Calvet Canopy roof top tent has been designed to bring more ease to the tallest users, with 40cm of extra head room.</p>
      <p>The new raised roof profile also increases air flow through the tent, giving a natural vent for warmer air to rise.</p>
    </div>
    <div class="foot" style="left:306px"><span class="foot-line"></span><span class="url-pill">WWW.VARNO.EXAMPLE</span><span class="page-num">05</span></div>
  </article>
</section>

<!-- Spread 3 -->
<section class="spread">
  <article class="page page-left">
    <div class="photo" style="left:0;top:0;width:290px;bottom:0;background:linear-gradient(180deg,#2c2418 0%,#8a5a22 30%,#e0a23a 45%,#a7652a 60%,#4a3420 100%)" role="img" aria-label="Golden sunset over rolling hills"></div>
    <h2 class="cfg-title" style="left:22px;top:22px">Configurator <span>Nomad</span></h2>
    <div class="sizes" style="left:22px;top:52px"><div class="sizes-head">AVAILABLE SIZES</div><div class="sizes-row"><b>STD</b>130 x 210 CM</div><div class="sizes-row"><b>XXL</b>160 x 210 CM</div></div>
    <div class="thumbs" style="left:306px;right:18px;top:18px;grid-template-columns:1fr 1fr;grid-template-rows:80px 80px">
      <div class="thumb" role="img" aria-label="Tent product photo, side view"><i></i></div>
      <div class="thumb" role="img" aria-label="Tent product photo, dark shell"><i></i></div>
      <div class="thumb box" role="img" aria-label="Tent product photo, interior"><i></i></div>
      <div class="thumb flat" role="img" aria-label="Tent product photo, closed shell"><i></i></div>
    </div>
    <div class="copy" style="left:306px;right:18px;top:200px">
      <p>Among the horizontally opening tents on the market, the Pierre Calvet Nomad roof top tent has the largest interior volume.</p>
      <p>With its larger overall internal space, the Nomad gives comfortable room for adults to sit upright at either end of the tent. With its full 360° windows, air moves freely through the tent.</p>
    </div>
    <div class="foot on-dark"><div class="brand"><i class="brand-mark"></i>VARNO Gearworks</div><span class="foot-line" style="opacity:0"></span><span class="url-pill">WWW.VARNO.EXAMPLE</span><span class="page-num">06</span></div>
  </article>
  <article class="page page-right">
    <div class="photo" style="left:0;top:0;right:0;height:135px;background:linear-gradient(180deg,#5a6a86 0%,#c48a5a 40%,#f0b060 55%,#6a4a36 80%,#2a2420 100%)" role="img" aria-label="Sunrise above a sea of clouds from a mountain top"></div>
    <h2 class="cfg-title" style="left:22px;top:22px">Configurator <span>Ranger</span></h2>
    <div class="thumbs" style="left:22px;right:22px;top:100px;grid-template-columns:repeat(4,1fr);height:86px">
      <div class="thumb" role="img" aria-label="Tent product photo, side view"><i></i></div>
      <div class="thumb" role="img" aria-label="Tent product photo, rear view"><i></i></div>
      <div class="thumb box" role="img" aria-label="Tent product photo, interior"><i></i></div>
      <div class="thumb flat" role="img" aria-label="Tent product photo, closed shell"><i></i></div>
    </div>
    <div class="copy" style="left:22px;right:22px;top:212px">
      <p>Built on the same concept as the Nomad with its horizontal opening and its 360° panoramic view, the Pierre Calvet Ranger is set apart by its luggage carrier which can easily carry a load of 25kg.</p>
      <p>The tent opens in less than 1 minute through four hydraulic cylinders mounted on bearings. It can be closed by one person in less than 1 minute, with the canvas held inside by an elastic band.</p>
    </div>
    <div class="foot"><div class="brand"><i class="brand-mark"></i>VARNO Gearworks</div><span class="foot-line"></span><span class="url-pill">WWW.VARNO.EXAMPLE</span><span class="page-num">07</span></div>
  </article>
</section>

</body>
</html>
```